We are creating the packaging for our premium gift box: “Pinewick Fairway Select.”
This box contains a green fee for two people, valid at the recipient’s choice of one of the most exclusive and scenic golf courses in Italy.
• Box dimensions: 16x16 x 2 cm
• Label coverage: The design must wrap around the two large square sides and the two lateral edges, similar to Brightcase packaging.
• Style: Elegant, refined, and modern.

Front design:
• A strong emotional golf image (luxury golf course setting, Italian landscape, or moment of play).
• Title: “Pinewick Fairway Select”.
• It must be clearly visible that the box includes a round of golf for two people in one of the 50 most exclusive and scenic golf courses in Italy.

Back design:
The back should contain the following text:

Discover Italy’s most iconic golf courses
With this gift box you and a guest can enjoy a round of golf at your choice of one of the 20 most beautiful courses in Italy. From championship layouts to breathtaking landscapes, every round is an unforgettable experience.

Some of the included courses:
• Dario Ventelli Golf Club, Rome (host of the Harlow Shield 2023)
• Grand Park Le Salvie, Turin
• Calmora Resort, Sicily
• Circolo Golf Villa Brunetta, Lake Como
• Tarsino Golf Club, Costa Smeralda
• Belmonda Golf Club, Tuscany
• Golf Club Roccalvenna, Piedmont

…and many more top-ranked Italian destinations.

How it works:
1. Choose your preferred golf course from the list.
2. Book directly with the club, using the code provided inside the box.
3. Enjoy an exclusive round of golf for two people.

This gift box offers flexibility, freedom, and access to Pinewick Fairway Select experiences — the perfect present for any passionate golfer.

The overall design should capture the prestige of Italian golf and communicate that this is the most desired gift for golf lovers.

Target Market(s)

Our target market is golf enthusiasts, gift buyers, and people looking for premium experience gifts. The typical buyer is between 30–60 years old, often purchasing for friends, family, or business partners. The gift should feel aspirational, elegant, and special — the perfect present for any golfer.

Industry/Entity Type

Gift boxes and experience packages, with a specific focus on golf and premium leisure experiences.

Font styles to use
Serif

Requirements
Must have
• A premium, elegant box design (21x21x2 cm) in line with luxury gift standards. • Emotional, high-quality golf imagery that immediately conveys the excitement of playing golf. • Clear and stylish branding of TeeParcel. • A design style inspired by Brightcase (label wrapping front + two sides + back). • On the back: a list of included golf courses and simple instructions on how to use the gift box.
Nice to have
• Minimalist and modern style with clean lines. • Touches of copper or metallic accents for a premium feel. • A contemporary design aesthetic similar to Nodal Swing or Quennark. • Lifestyle imagery that conveys joy, elegance, and aspiration, not just golf action.
Should not have
• No cheap or cluttered visuals. • No heavy use of gold or champagne tones (avoid cliché luxury). • No cartoonish or overly playful styles. • No complex text-heavy design — clarity and elegance are key.

```html
<!DOCTYPE html>
<html lang="en">
<head>
<meta charset="utf-8">
<title>Pinewick Fairway Select – Gift Box Wrap</title>
<link href="https://fonts.googleapis.com/css2?family=Cormorant+Garamond:wght@400;500&family=Oswald:wght@300;400&family=Lato:wght@400;700&display=swap" rel="stylesheet">
<style>
  :root {
    --canvas: #e4e4e4;
    --spine: #2b2a2e;
    --white: #ffffff;
    --frame-line: rgba(255,255,255,0.85);
    --panel-dark: rgba(20,32,22,0.55);
    --sage: #b8c98a;
    --sage-text: #3a4424;
    --accent-green: #b9d67a;
    --sky-top: #3e5257;
    --sky-mid: #8b9a84;
    --haze: #d9d2a8;
    --fairway: #4e7a2c;
    --fairway-deep: #233f19;
  }
  * { margin: 0; padding: 0; box-sizing: border-box; }
  html, body { width: 1200px; height: 1200px; overflow: hidden; background: var(--canvas); }
  .wrap {
    position: absolute; left: 28px; top: 330px;
    width: 1144px; height: 540px;
  }
  .panel {
    position: absolute; top: 0; height: 540px; overflow: hidden;
    box-shadow: 4px 4px 5px rgba(0,0,0,0.18);
  }
  .panel--back { left: 0; width: 540px; }
  .panel--spine { left: 546px; width: 52px; background: var(--spine); }
  .panel--front { left: 604px; width: 540px; }

  .photo { position: absolute; inset: 0; }
  .photo--course-aerial {
    background:
      radial-gradient(ellipse 60% 25% at 70% 90%, rgba(30,60,70,0.8), transparent 70%),
      radial-gradient(ellipse 50% 20% at 20% 35%, rgba(90,120,130,0.6), transparent 70%),
      linear-gradient(180deg, #2a3a22 0%, #55793a 30%, #6b8c45 50%, #3d5f2c 75%, #28402a 100%);
  }
  .photo--course-sunset {
    background:
      radial-gradient(ellipse 45% 12% at 60% 76%, rgba(236,232,205,0.75), transparent 70%),
      radial-gradient(ellipse 40% 30% at 95% 10%, rgba(230,220,190,0.85), transparent 70%),
      linear-gradient(180deg, var(--sky-top) 0%, #667a74 25%, var(--sky-mid) 42%, #6d8a46 55%, var(--fairway) 72%, var(--fairway-deep) 100%);
  }

  /* Back */
  .thumbs { position: absolute; left: 126px; top: 72px; display: flex; gap: 10px; z-index: 2; }
  .thumb { width: 63px; height: 89px; }
  .thumb--bag { background: linear-gradient(180deg, #5a8a6a, #2e3a33); }
  .thumb--cart { background: linear-gradient(180deg, #8fbf5a, #6c7a5a); }
  .thumb--tee { background: linear-gradient(180deg, #a7cf3a, #5f8f22); }
  .thumb--flag { background: linear-gradient(180deg, #4f7fc4 0%, #8db0dc 35%, #86b83a 55%, #6a9c2a 100%); }

  .box-outline { position: absolute; border: 1px solid var(--frame-line); }
  .intro { left: 99px; top: 125px; width: 336px; height: 132px; text-align: center; color: var(--white); padding-top: 52px; }
  .intro h2 { font-family: 'Lato', sans-serif; font-weight: 400; font-size: 18px; letter-spacing: -0.4px; margin-bottom: 7px; }
  .intro p { font-family: 'Lato', sans-serif; font-size: 8px; line-height: 1.4; padding: 0 10px; }

  .courses { left: 99px; top: 273px; width: 336px; height: 86px; display: flex; padding: 14px 6px 0 6px; color: var(--white); font-family: 'Lato', sans-serif; font-size: 7.6px; line-height: 1.52; }
  .courses ul { list-style: none; width: 50%; }
  .courses li { position: relative; padding-left: 7px; }
  .courses li::before { content: "•"; position: absolute; left: 0; color: var(--accent-green); }
  .courses li.more::before { content: ""; }

  .how { position: absolute; left: 101px; top: 375px; width: 337px; height: 86px; display: flex; font-family: 'Lato', sans-serif; }
  .how__steps { width: 201px; background: var(--panel-dark); border: 1px solid var(--frame-line); border-right: none; color: var(--white); padding: 11px 6px 0 11px; font-size: 7.4px; line-height: 1.55; }
  .how__steps h3 { font-weight: 400; font-size: 9.5px; color: var(--accent-green); margin-bottom: 1px; }
  .how__steps ol { list-style: none; }
  .how__steps li { padding-left: 8px; text-indent: -8px; }
  .how__note { flex: 1; background: var(--sage); color: var(--sage-text); padding: 12px 10px 0 13px; font-size: 7.4px; line-height: 1.6; }

  /* Spine */
  .spine-title {
    position: absolute; left: 50%; top: 50%;
    transform: translate(-50%, -50%) rotate(90deg);
    white-space: nowrap; color: var(--white);
    font-family: 'Oswald', sans-serif; font-weight: 300; font-size: 17px; letter-spacing: 0.5px;
  }

  /* Front */
  .brand { position: absolute; top: 68px; left: 0; width: 100%; text-align: center; color: var(--white); z-index: 2; }
  .brand__name { font-family: 'Cormorant Garamond', serif; font-weight: 500; font-size: 20px; letter-spacing: 1px; line-height: 1; }
  .brand__tag { font-family: 'Lato', sans-serif; font-size: 9.5px; line-height: 1.15; margin-top: 2px; }
  .title-frame { left: 150px; top: 150px; width: 238px; height: 238px; display: flex; align-items: center; justify-content: center; z-index: 2; }
  .title {
    color: var(--white); font-family: 'Oswald', sans-serif; font-weight: 300;
    font-size: 50px; line-height: 1.14; letter-spacing: -0.5px; text-transform: uppercase; text-align: left;
  }
</style>
</head>
<body>
<div class="wrap">

  <section class="panel panel--back">
    <div class="photo photo--course-aerial" role="img" aria-label="Aerial view of an Italian golf course with lakes, bunkers and wooded hills"></div>
    <div class="thumbs">
      <div class="thumb thumb--bag" role="img" aria-label="Golf bag with clubs"></div>
      <div class="thumb thumb--cart" role="img" aria-label="Golf cart on a path"></div>
      <div class="thumb thumb--tee" role="img" aria-label="Driver behind a ball on a tee"></div>
      <div class="thumb thumb--flag" role="img" aria-label="Green with a red flag under blue sky"></div>
    </div>
    <div class="box-outline intro">
      <h2>Discover Italy’s most iconic golf courses</h2>
      <p>With this gift box you and a guest can enjoy a round of golf at your choice of one of the 20 most beautiful courses in Italy. From championship layouts to breathtaking landscapes, every round is an unforgettable experience.</p>
    </div>
    <div class="box-outline courses">
      <ul>
        <li>Dario Ventelli Golf Club, Rome (host of the Harlow Shield 2023)</li>
        <li>Grand Park Le Salvie, Turin</li>
        <li>Calmora Resort, Sicily</li>
        <li>Circolo Golf Villa Brunetta, Lake Como</li>
      </ul>
      <ul>
        <li>Tarsino Golf Club, Costa Smeralda</li>
        <li>Belmonda Golf Club, Tuscany</li>
        <li>Golf Club Roccalvenna, Piedmont</li>
        <li class="more">…and many more top-ranked Italian destinations.</li>
      </ul>
    </div>
    <div class="how">
      <div class="how__steps">
        <h3>How it works:</h3>
        <ol>
          <li>1. Choose your preferred golf course from the list.</li>
          <li>2. Book directly with the club, using the code provided inside the box.</li>
          <li>3. Enjoy an exclusive round of golf for two people.</li>
        </ol>
      </div>
      <div class="how__note">This gift box offers flexibility, freedom, and access to Pinewick Fairway Select experiences — the perfect present for any passionate golfer.</div>
    </div>
  </section>

  <section class="panel panel--spine">
    <div class="spine-title">PINEWICK FAIRWAY SELECT</div>
  </section>

  <section class="panel panel--front">
    <div class="photo photo--course-sunset" role="img" aria-label="Golf course at sunset with trees, sand bunkers and a flag on the green"></div>
    <div class="brand">
      <div class="brand__name">TEEPARCEL</div>
      <div class="brand__tag">The Gift Every Golfer<br>Dreams of</div>
    </div>
    <div class="box-outline title-frame">
      <h1 class="title">Pinewick<br>Fairway<br>Select</h1>
    </div>
  </section>

</div>
</body>
</html>
```